Redesign of Business Card to look more professional and stand out

Business card design. You can lean more about our company by going to dkrfabworks.example. Raised letters would be nice. Company name & Address
DK&R
418 Wendlow Ridge Drive, Suite 340
Birmingham, AL 35242

You can use my name and title: Glenn Harwick
Business Development Manager

Target Market(s)

Heavy Industrial market, i.e. utilities, chemical plants, paper mills, construction companies

Industry/Entity Type

Construction

Contact Information for Business Card

We provide Project Management & Project Support Services

Font styles to use
Serif

Requirements
Must have
• Company name & Address
• DK&R
• 418 Wendlow Ridge Drive, Suite 340
• Birmingham, AL 35242
Nice to have
• ideas for the back of the card
Should not have
• no crazy colors. needs to look professional and standout.

```html
<!DOCTYPE html>
<html lang="en">
<head>
<meta charset="utf-8">
<title>DK&amp;R Business Card</title>
<link rel="stylesheet" href="https://fonts.googleapis.com/css2?family=Source+Serif+4:wght@400;600&display=swap">
<style>
  :root {
    --navy: #1c3466;
    --card-white: #f7f7f7;
    --ink: #3b3b3b;
    --title-tint: #dfe5f1;
    --stage: #e8e5e0;
    --rule: #7a89a8;
    --serif: "Source Serif 4", Georgia, serif;
  }
  * { margin: 0; padding: 0; box-sizing: border-box; }
  html, body {
    width: 1200px; height: 1023px; overflow: hidden;
    background: var(--stage);
  }
  .canvas { position: relative; width: 1200px; height: 1023px; }

  .card {
    position: absolute;
    width: 620px; height: 354px;
    border-radius: 4px;
    box-shadow: 0 10px 28px rgba(0,0,0,.18), 0 2px 5px rgba(0,0,0,.12);
    overflow: hidden;
    font-family: var(--serif);
  }

  /* Front */
  .card-front { left: 70px; top: 70px; background: var(--card-white); }
  .front-name {
    position: absolute; left: 40px; top: 28px;
    font-weight: 600; font-size: 100px; line-height: 1;
    color: var(--navy);
    white-space: nowrap;
  }
  .name-band {
    position: absolute; left: 0; right: 0; top: 156px; height: 74px;
    background: var(--navy);
    padding: 11px 40px;
    color: #fff;
  }
  .person-name {
    font-weight: 600; font-size: 26px; line-height: 1.1;
    letter-spacing: 1.5px; text-transform: uppercase;
  }
  .person-title {
    font-weight: 400; font-size: 15px; line-height: 1.5;
    color: var(--title-tint);
  }
  .contact-list {
    position: absolute; left: 40px; top: 244px;
    list-style: none;
    font-size: 14.5px; color: var(--ink);
  }
  .contact-list li {
    display: flex; align-items: center; justify-content: flex-end;
    gap: 9px; height: 23px; white-space: nowrap;
  }
  .contact-list svg { width: 15px; height: 15px; flex: none; }
  .divider {
    position: absolute; left: 352px; top: 248px; height: 82px;
    border-left: 1px dotted var(--rule);
  }
  .address {
    position: absolute; left: 372px; top: 246px;
    font-style: normal; font-size: 14.5px; line-height: 23px;
    color: var(--ink); white-space: nowrap;
  }

  /* Back */
  .card-back {
    left: 520px; top: 590px; background: var(--navy);
    display: flex; align-items: center; justify-content: center;
  }
  .back-name {
    font-weight: 600; font-size: 120px; line-height: 1;
    color: #fff; white-space: nowrap;
  }
</style>
</head>
<body>
<main class="canvas">

  <section class="card card-front" aria-label="Business card front">
    <div class="front-name">DK&amp;R</div>

    <div class="name-band">
      <div class="person-name">Glenn Harwick</div>
      <div class="person-title">Business Development Manager</div>
    </div>

    <ul class="contact-list">
      <li>205-555-0147
        <svg viewBox="0 0 16 16" aria-hidden="true"><circle cx="8" cy="8" r="8" fill="#1c3466"/><path d="M5.2 4.2l1.4-.3.8 1.9-.9.7a5 5 0 0 0 2.9 2.9l.7-.9 1.9.8-.3 1.4c-3.8.2-6.8-2.8-6.5-6.5z" fill="#fff"/></svg>
      </li>
      <li>205-555-0148
        <svg viewBox="0 0 16 16" aria-hidden="true"><circle cx="8" cy="8" r="8" fill="#1c3466"/><rect x="4.5" y="6.5" width="7" height="4" fill="#fff"/><rect x="5.8" y="4.2" width="4.4" height="2" fill="#fff"/><rect x="5.8" y="9.5" width="4.4" height="2.4" fill="#fff" stroke="#1c3466" stroke-width=".6"/></svg>
      </li>
      <li>info@dkrprojectmgt.example
        <svg viewBox="0 0 16 16" aria-hidden="true"><circle cx="8" cy="8" r="8" fill="#1c3466"/><rect x="4" y="5.2" width="8" height="5.6" fill="#fff"/><path d="M4 5.4l4 3 4-3" fill="none" stroke="#1c3466" stroke-width=".9"/></svg>
      </li>
      <li>www.dkrfabworks.example
        <svg viewBox="0 0 16 16" aria-hidden="true"><circle cx="8" cy="8" r="8" fill="#1c3466"/><g fill="none" stroke="#fff" stroke-width=".9"><circle cx="8" cy="8" r="4.2"/><ellipse cx="8" cy="8" rx="1.8" ry="4.2"/><path d="M3.8 8h8.4"/></g></svg>
      </li>
    </ul>

    <div class="divider"></div>

    <address class="address">
      418 Wendlow Ridge Drive,<br>
      Suite 340 Birmingham,<br>
      AL 35242
    </address>
  </section>

  <section class="card card-back" aria-label="Business card back">
    <div class="back-name">DK&amp;R</div>
  </section>

</main>
</body>
</html>
```